Business card and stationary for Intellectual Property Consultant & Law Firm
Harborline Claims Omniworks
Business card and stationary for Intellectual Property Consultant & Law Firm - Law
Creative Brief
Simple
Dorin Makalesu
President Director
Kelor Business Center 11th Floor Jl. Raya Wibisana Kav.37-38 Jakarta Pusat 10485, Indonesia
office@harborlineclaims.example
www.harborlineclaims.example
Member: OQRU, EKLM, UVBO, WDGF
Please add Intellectual Property Rights Consultant & Law Firm for letterhead additional of our email : hbl42@harborlineclaims.example; marks@harborlineclaims.example
please add Branch office : Surabaya (+6231) 480 3926 Medan (+6261) 819 4057 Solo (+62271) 634 918
trelvorin trelvorin
Dear All, Please provide me the stationary : letterhead, envelope, cds, ballpoint, ruler, stamps, usb sticks etc
dunmoral dunmoral
Please upload Ai or eps file of your logo thankyou
Please add : Intellectual Property Rights Consultant & Law Firm in envelope and letter head.

```html
<!DOCTYPE html>
<html lang="en">
<head>
<meta charset="utf-8">
<title>Harborline Claims Omniworks – Business Card</title>
<link rel="stylesheet" href="https://fonts.googleapis.com/css2?family=Open+Sans:wght@400;600&display=swap">
<style>
  :root {
    --bg: #ecebe8;
    --card: #ffffff;
    --ink: #4a4a4c;
    --ink-soft: #6d6d70;
    --accent-pink: #e0317a;
    --accent-gold: #d8a53a;
    --band-grey: #8f8f92;
    --band-grey-dark: #7a7a7d;
  }
  * { box-sizing: border-box; margin: 0; padding: 0; }
  html, body {
    width: 1200px; height: 912px; overflow: hidden;
    background: var(--bg);
    font-family: "Open Sans", sans-serif;
    color: var(--ink);
  }
  .stage {
    position: relative; width: 1200px; height: 912px;
    display: flex; align-items: center; justify-content: center; gap: 40px;
  }
  .card {
    position: relative; width: 540px; height: 310px;
    background: var(--card); border-radius: 18px; overflow: hidden;
    box-shadow: 0 2px 6px rgba(0,0,0,.12);
  }
  .wordmark {
    display: flex; align-items: center; gap: 10px;
    font-weight: 600; color: var(--ink); letter-spacing: -0.2px; line-height: 1.05;
  }
  .wordmark-dot { width: 14px; height: 14px; background: var(--accent-pink); flex: none; }
  .card-front { display: flex; align-items: center; justify-content: center; }
  .card-front .wordmark { font-size: 26px; }
  .card-back .band { position: absolute; inset: 0; }
  .card-back .wordmark {
    position: absolute; right: 34px; top: 46px; font-size: 19px; text-align: right;
  }
  .contact { position: absolute; left: 30px; top: 112px; }
  .contact-name { color: var(--accent-pink); font-weight: 600; font-size: 15px; }
  .contact-role { font-size: 17px; color: var(--ink); margin-bottom: 8px; }
  .contact-line {
    display: flex; align-items: center; gap: 6px;
    font-size: 9.5px; color: var(--ink-soft); line-height: 14px;
  }
  .contact-line svg { width: 9px; height: 9px; flex: none; }
  .address { font-size: 9.5px; color: var(--ink-soft); line-height: 13px; margin-bottom: 2px; }
</style>
</head>
<body>
<main class="stage">
  <section class="card card-front" aria-label="Business card front">
    <div class="wordmark"><span class="wordmark-dot"></span><span>Harborline Claims Omniworks</span></div>
  </section>

  <section class="card card-back" aria-label="Business card back">
    <svg class="band" viewBox="0 0 540 310" preserveAspectRatio="none" aria-hidden="true">
      <path d="M0,262 C170,262 360,250 540,165 L540,310 L0,310 Z" fill="var(--band-grey)"/>
      <path d="M0,262 C170,262 360,250 540,165" fill="none" stroke="var(--band-grey-dark)" stroke-width="3"/>
      <path d="M120,248 C250,246 390,232 540,150" fill="none" stroke="var(--accent-gold)" stroke-width="3"/>
    </svg>

    <div class="wordmark"><span>Harborline Claims<br>Omniworks</span></div>

    <div class="contact">
      <p class="contact-name">Merin Tavell-Ruse</p>
      <p class="contact-role">Consultant</p>
      <p class="address">14 Harbor Tower Floor<br>Lantern Road JKT</p>
      <p class="contact-line">
        <svg viewBox="0 0 10 10"><path d="M5 0.5a3 3 0 0 0-3 3c0 2.3 3 6 3 6s3-3.7 3-6a3 3 0 0 0-3-3z" fill="var(--accent-pink)"/></svg>
        012 555 0142
      </p>
      <p class="contact-line">
        <svg viewBox="0 0 10 10"><path d="M2 1l2 2-1 1.2c.6 1.2 1.5 2.1 2.8 2.8L7 6l2 2-1.3 1.5C4.5 9 1 5.5.5 2.3z" fill="var(--accent-gold)"/></svg>
        012 555 0142
      </p>
      <p class="contact-line">
        <svg viewBox="0 0 10 10"><rect x="0.5" y="2" width="9" height="6" rx="1" fill="var(--accent-pink)"/><path d="M1 2.5l4 3 4-3" stroke="#fff" stroke-width=".8" fill="none"/></svg>
        merin@harborlineclaims.example
      </p>
      <p class="contact-line">
        <svg viewBox="0 0 10 10"><circle cx="5" cy="5" r="4.3" fill="none" stroke="var(--accent-pink)" stroke-width="1.2"/><path d="M.7 5h8.6M5 .7c-2 2.5-2 6 0 8.6M5 .7c2 2.5 2 6 0 8.6" stroke="var(--accent-pink)" stroke-width=".8" fill="none"/></svg>
        www.harborlineclaims.example
      </p>
    </div>
  </section>
</main>
</body>
</html>
```